CalmHarbor Homepage and Landing Pages

Please see detailed brief.

CalmHarbor is Australia’s newest online therapy and mental health service. We allow patients from across australia to connect with Mental health practitioners from across Australia. Our mission is to remove the friction in gaining support for mental health related issues.

Number of Pages Required

1 page

Font styles to use
Sans Serif

Colors
33a6d7
0293ce
3277b5
0255a3
acd136
9bcb3c

Requirements
Must have
• Please see detailed brief.
Nice to have
• Please see detailed brief
Should not have

```html
<!DOCTYPE html>
<html lang="en">
<head>
<meta charset="utf-8">
<title>CalmHarbor — Contact</title>
<link rel="stylesheet" href="https://fonts.googleapis.com/css2?family=Open+Sans:wght@600;700&family=Roboto:wght@400;500;700&display=swap">
<style>
:root{
  --sky:#33a6d7;
  --azure:#0293ce;
  --mid-blue:#3277b5;
  --deep-blue:#0255a3;
  --lime:#acd136;
  --lime-dark:#9bcb3c;
  --ink:#1c1c1c;
  --nav-ink:#3a3a3a;
  --panel:#f4f5f8;
  --field:#e4e7ee;
  --white:#ffffff;
}
*{box-sizing:border-box;margin:0;padding:0}
html,body{width:1200px;height:3640px;overflow:hidden;background:var(--white)}
body{position:relative;font-family:'Roboto',Arial,sans-serif;color:var(--ink)}
.abs{position:absolute}

/* Header */
.site-header{position:absolute;left:0;top:0;width:1200px;height:90px;background:#f2f3f6;box-shadow:0 3px 6px rgba(0,0,0,.25);z-index:2}
.brand{position:absolute;left:28px;top:22px;display:flex;align-items:center;gap:12px;font-family:'Roboto',Arial,sans-serif;font-weight:400;font-size:38px;color:var(--nav-ink)}
.brand-dot{width:24px;height:24px;border-radius:50%;background:var(--azure)}
.main-nav{position:absolute;left:408px;top:26px;width:632px;height:38px;border-bottom:2px solid #555}
.main-nav a{position:absolute;top:0;font-size:21px;color:var(--nav-ink);text-decoration:none}
.main-nav a.current{color:var(--deep-blue);font-weight:700}
.btn-signup{position:absolute;left:1071px;top:17px;width:111px;height:44px;background:var(--lime);color:var(--white);font-size:21px;display:flex;align-items:center;justify-content:center;border-radius:3px}

/* Hero contact */
.hero{position:absolute;left:0;top:90px;width:1200px;height:1119px}
.hero-photo{position:absolute;inset:0;background:linear-gradient(120deg,#1f4f8f 0%,#2d65a6 40%,#4a7fba 65%,#2a5d9c 100%)}
.hero-title{position:absolute;left:120px;top:158px;font-family:'Open Sans',Arial,sans-serif;font-weight:700;font-size:43px;color:var(--white)}
.hero-text{position:absolute;left:120px;top:214px;width:480px;font-size:21px;line-height:25px;color:var(--white)}
.social{position:absolute;top:287px;width:47px;height:47px;border:3px solid var(--white);border-radius:8px}
.field-label{position:absolute;left:119px;font-size:20px;color:var(--white)}
.field{position:absolute;left:119px;background:var(--field);border-radius:5px;opacity:.95}
.btn-send{position:absolute;left:933px;top:850px;width:159px;height:40px;background:var(--white);border-radius:4px;font-size:27px;display:flex;align-items:center;justify-content:center;color:var(--ink)}

/* Offer */
.offer-title{position:absolute;left:0;width:1200px;top:1335px;text-align:center;font-family:'Open Sans',Arial,sans-serif;font-weight:700;font-size:44px;color:var(--deep-blue)}
.offer-item{position:absolute;top:1474px;width:240px;text-align:center;font-size:21px;line-height:25px}
.offer-photo{width:194px;height:194px;border-radius:50%;margin:0 auto 20px;border:2px solid #bbb}

/* Feature rows */
.feature{position:absolute;left:0;width:1192px;height:600px}
.feature-text{position:absolute;top:0;width:591px;height:600px}
.feature-photo{position:absolute;top:0;width:600px;height:600px}
.feature h2{position:absolute;font-family:'Open Sans',Arial,sans-serif;font-weight:700;font-size:30px;color:var(--ink)}
.feature p{position:absolute;width:390px;font-size:21px;line-height:25px}
.btn-more{position:absolute;width:240px;height:62px;background:var(--lime);color:var(--white);font-size:27px;display:flex;align-items:center;justify-content:center;border-radius:3px}
</style>
</head>
<body>

<header class="site-header">
  <div class="brand"><span class="brand-dot"></span>CalmHarbor</div>
  <nav class="main-nav">
    <a style="left:0">Home</a>
    <a style="left:113px">About</a>
    <a style="left:228px">Our Team</a>
    <a style="left:376px">Practitioners</a>
    <a class="current" style="left:556px">Contact</a>
  </nav>
  <div class="btn-signup">Sign Up</div>
</header>

<section class="hero">
  <div class="hero-photo" role="img" aria-label="Therapist taking notes during a session with a client, under a blue tint"></div>
  <h1 class="hero-title">Tell us what is happening</h1>
  <p class="hero-text">Lorem ipsum dolor sit amet, consectetur adipiscing elit. Maecenas varius tortor nibh, sit</p>
  <span class="social" style="left:120px" aria-label="Social link"></span>
  <span class="social" style="left:196px" aria-label="Social link"></span>
  <span class="field-label" style="top:404px">Name</span>
  <div class="field" style="top:434px;width:411px;height:41px"></div>
  <span class="field-label" style="top:500px">E-mal</span>
  <div class="field" style="top:530px;width:411px;height:41px"></div>
  <div class="field" style="top:602px;width:973px;height:213px"></div>
  <div class="btn-send">Send</div>
</section>

<h2 class="offer-title">What we offer</h2>
<div class="offer-item" style="left:84px">
  <div class="offer-photo" role="img" aria-label="Portrait of a bearded professional in a grey blazer" style="background:linear-gradient(#e8e8e8,#a9a9ab)"></div>150 Profesionals
</div>
<div class="offer-item" style="left:462px">
  <div class="offer-photo" role="img" aria-label="Smiling couple sitting together" style="background:linear-gradient(#9aa7b5,#c9c1b3)"></div>2000 Customers
</div>
<div class="offer-item" style="left:860px">
  <div class="offer-photo" role="img" aria-label="Two people holding hands in comfort" style="background:linear-gradient(#8a8e97,#c79a80)"></div>10 Years of<br>experience
</div>

<section class="feature" style="top:1840px">
  <div class="feature-text" style="left:0;background:var(--panel)">
    <h2 style="left:106px;top:116px">Find your confidence</h2>
    <p style="left:107px;top:156px">Lorem ipsum dolor sit amet, consectetur adipiscing elit. Maecenas varius tortor nibh, sit amet tempor nibh finibus et. Aenean eu enim justo.</p>
    <div class="btn-more" style="left:246px;top:293px">Read More</div>
  </div>
  <div class="feature-photo" style="left:592px;background:linear-gradient(135deg,#d9dde0,#8f8d8a 55%,#6b5a48)" role="img" aria-label="Confident man in a blazer with coffee at a laptop"></div>
</section>

<section class="feature" style="top:2440px">
  <div class="feature-photo" style="left:0;width:591px;background:linear-gradient(135deg,#d8d4cf,#b89b86 50%,#e3c9c6)" role="img" aria-label="Happy couple laughing together at breakfast"></div>
  <div class="feature-text" style="left:592px;width:600px;background:var(--white)">
    <h2 style="left:113px;top:152px">Love yourself again</h2>
    <p style="left:113px;top:192px">Lorem ipsum dolor sit amet, consectetur adipiscing elit. Maecenas varius tortor nibh, sit amet tempor nibh finibus et. Aenean eu enim justo.</p>
    <div class="btn-more" style="left:252px;top:330px">Read More</div>
  </div>
</section>

<section class="feature" style="top:3040px">
  <div class="feature-text" style="left:0;background:var(--panel)">
    <h2 style="left:106px;top:172px">Fight anxiety</h2>
    <p style="left:106px;top:212px">Lorem ipsum dolor sit amet, consectetur adipiscing elit. Maecenas varius tortor nibh, sit amet tempor nibh finibus et. Aenean eu enim justo.</p>
    <div class="btn-more" style="left:247px;top:345px">Read More</div>
  </div>
  <div class="feature-photo" style="left:592px;background:linear-gradient(160deg,#f2f2f2,#e0dcd8 50%,#c0603c 80%,#b9876e)" role="img" aria-label="Relaxed man leaning back in an armchair with hands behind his head"></div>
</section>

</body>
</html>
```